Business Card Design Project

We have a logo, but would like to expand the use of it into a business card design. We are a B2B technology exchange platform for institutional investors to invest excess cash into short term assets matching their credit and pricing parameters. The assets are fractionalized and investors invest in portions.

Our customers are large, institutional, financial companies who are a bit traditional. We are high energy rebels with a cause...we are a disruptive technology and want to be viewed as a game changer but we need to present an image of trustworthiness and secure.

We are open not only to the image design but the material, die cut, etc. but want to stay in the traditional size of a business card.

We have other formats of the logo if needed. Our website is www.brambleharbor.com

I have posted a powerpoint template that we have been using.  This should not be considered the template we will use (after business cards we will have another project to incorporate business card design into powerpoint template) but just to give you a flavor of where we have been and have used in the past.

Target Market(s)

Institutional investors, asset managers, large fund institutions

Industry/Entity Type

Financial

Requirements
Must have
• Our logo
Traditional size
Nice to have
• unique use of logo, unique material, die cut, etc
Crisp, clean look
Use of both sides of card in a creative manner

```html
<!DOCTYPE html>
<html lang="en">
<head>
<meta charset="utf-8">
<title>Bramble Harbor – Business Card</title>
<link href="https://fonts.googleapis.com/css2?family=Open+Sans:wght@400;600;700&display=swap" rel="stylesheet">
<style>
  :root {
    --bg: #e9e7e3;
    --card: #f4f4f3;
    --orange: #d7820f;
    --ink: #4a4a4a;
    --ink-soft: #6a6a6a;
    --faint: #e2e2e1;
    --shadow: rgba(0,0,0,0.18);
  }
  * { margin: 0; padding: 0; box-sizing: border-box; }
  html, body { width: 1200px; height: 900px; overflow: hidden; }
  body {
    background: var(--bg);
    font-family: "Open Sans", Arial, sans-serif;
    color: var(--ink);
    position: relative;
  }
  .card {
    position: absolute;
    width: 600px;
    height: 343px;
    background: var(--card);
    border-radius: 4px;
    box-shadow: 0 6px 18px var(--shadow);
    overflow: hidden;
  }
  .brand-name {
    font-weight: 700;
    color: var(--ink);
    letter-spacing: 0.04em;
    text-transform: uppercase;
    display: flex;
    align-items: center;
    gap: 10px;
  }
  .brand-dot {
    width: 16px; height: 16px;
    border-radius: 50%;
    background: var(--orange);
  }

  /* Back side */
  .card-back { left: 50px; top: 70px; }
  .card-back .accent-band {
    position: absolute; left: 0; top: 0;
    width: 190px; height: 100%;
    background: var(--orange);
  }
  .card-back .back-info {
    position: absolute; right: 40px; top: 70px;
    text-align: right;
  }
  .card-back .brand-name { font-size: 26px; justify-content: flex-end; }
  .card-back .website {
    margin-top: 18px;
    font-size: 15px; font-weight: 600;
    color: var(--orange);
  }
  .card-back .social {
    margin-top: 6px;
    font-size: 14px;
    color: var(--ink-soft);
    display: flex; align-items: center; justify-content: flex-end; gap: 6px;
  }
  .social-square { width: 12px; height: 12px; background: #2c6a9b; }

  /* Front side */
  .card-front { left: 550px; top: 480px; }
  .card-front .faint-circle {
    position: absolute; right: -60px; top: -80px;
    width: 300px; height: 300px;
    border-radius: 50%;
    background: var(--faint);
  }
  .card-front .brand-name {
    position: absolute; left: 36px; top: 60px;
    font-size: 24px;
  }
  .card-front .address {
    position: absolute; right: 32px; top: 40px;
    font-size: 12px; line-height: 1.45;
    color: var(--ink-soft);
    text-align: right;
  }
  .card-front .person { position: absolute; left: 36px; top: 150px; }
  .person-name { font-size: 24px; color: var(--orange); font-weight: 400; }
  .person-title { font-size: 14px; color: var(--ink-soft); margin-top: 2px; }
  .contact-list {
    position: absolute; left: 36px; top: 240px;
    list-style: none;
    font-size: 13px; line-height: 1.5;
    color: var(--ink-soft);
  }
  .contact-list .label {
    display: inline-block; width: 18px;
    color: var(--orange); font-weight: 700;
  }
</style>
</head>
<body>
  <section class="card card-back" aria-label="Card back">
    <div class="accent-band"></div>
    <div class="back-info">
      <div class="brand-name"><span class="brand-dot"></span>Bramble Harbor</div>
      <div class="website">www.BrambleHarbor.com</div>
      <div class="social"><span class="social-square"></span>peterlindqvist</div>
    </div>
  </section>

  <section class="card card-front" aria-label="Card front">
    <div class="faint-circle"></div>
    <div class="brand-name"><span class="brand-dot"></span>Bramble Harbor</div>
    <address class="address">
      2180 Fernside Ridge Road,<br>
      Suite 412<br>
      Oakmere Village, CA 90000
    </address>
    <div class="person">
      <div class="person-name">Peter Lindqvist</div>
      <div class="person-title">President &amp; CEO</div>
    </div>
    <ul class="contact-list">
      <li><span class="label">T</span>805.555.0146</li>
      <li><span class="label">M</span>818.555.0172</li>
      <li><span class="label">E</span>peterlindqvist@brambleharbor.com</li>
    </ul>
  </section>
</body>
</html>
```